Talfunkeln mit Rike Solmsen - ein Flyer der Lust auf Abenteuer macht
Zielgruppe
Ihr Lieben Designenden, ich möchte den Flyer auch als Visitenkarte verwenden..... bitte empfehlt mir dazu eine der Größen die ich unten angegeben habe....
Der Flyer soll Lust machen unterwegs zu sein, Freude zu haben, sich weiterzuentwickeln und einfach ne super gute Zeit zum Haben. Also lasst es krachen.
Wandertouren, Trekkingreisen, Naturerlebnisse
Zielgruppe: Frauen und Männer im Alter zwischen 40 und 60 Jahren
Aufgabenstellung
12x12 cm - 4 Seiten - siehe Skizzen - die Schriften und Designelemente können schwarz, weiß und pink wie im Logo sein. Ich liebe auch den Holzwandlook.
Wandertouren - gemeinsam unterwegs sein
Trekkingreisen - erfülle Deine Träume
Naturerlebnisse - Zeit für Dich und Deine Seele
lokal & international
Inspirationen für Dich und Dein Leben
Rike Solmsen
International Mountain Leader
Diplom-Sozialpädagogin
KaviRen Lehrerin (1.Dan)
www.talfunkeln-beispiel.eu
info@talfunkeln-beispiel.eu
Platz für den QR Code als Link für die Website

```html
<!DOCTYPE html>
<html lang="de">
<head>
<meta charset="utf-8">
<title>Talfunkeln – Lokal &amp; international</title>
<link rel="stylesheet" href="https://fonts.googleapis.com/css2?family=Fira+Sans+Condensed:wght@400;500&display=swap">
<style>
  :root {
    --pink: #ea4f6e;
    --white: #ffffff;
    --ink: #111111;
    --strip: #1b1b1b;
  }
  * { margin: 0; padding: 0; box-sizing: border-box; }
  html, body { width: 848px; height: 1200px; overflow: hidden; background: var(--pink); }
  .flyer {
    position: relative;
    width: 848px;
    height: 1200px;
    background: var(--pink);
    font-family: "Fira Sans Condensed", "Arial Narrow", sans-serif;
    overflow: hidden;
  }
  .headline {
    position: absolute;
    left: 0;
    width: 460px;
    top: 78px;
    text-align: center;
    color: var(--ink);
    font-weight: 500;
    font-size: 49px;
    line-height: 46px;
    letter-spacing: -0.5px;
  }
  .offer {
    position: absolute;
    left: 36px;
    color: var(--white);
    font-size: 30px;
    line-height: 39px;
    letter-spacing: -0.6px;
  }
  .offer--hiking { top: 333px; }
  .offer--trekking { top: 561px; }
  .offer--nature { top: 718px; }
  .film-strip {
    position: absolute;
    left: 493px;
    top: 0;
    width: 355px;
    height: 1200px;
    background: var(--strip);
  }
  .photo {
    position: absolute;
    left: 521px;
    width: 313px;
  }
  .photo--hikers {
    top: 0; height: 389px;
    background: linear-gradient(180deg, #3f86e0 0%, #8fb9e8 40%, #b9b6a8 65%, #d8d3c8 100%);
  }
  .photo--poppies {
    top: 401px; height: 396px;
    background: linear-gradient(180deg, #6d90b7 0%, #6a6a66 30%, #b4b1aa 55%, #e2b41d 80%, #d9a50f 100%);
  }
  .photo--valley {
    top: 808px; height: 392px;
    background: linear-gradient(180deg, #d5dde3 0%, #aab8c4 35%, #6e7e74 60%, #3f5b2e 85%, #2f4522 100%);
  }
  .tagline-box {
    position: absolute;
    left: 36px;
    top: 954px;
    width: 417px;
    height: 212px;
    background: var(--white);
  }
  .tagline {
    position: absolute;
    right: 30px;
    top: 62px;
    text-align: right;
    color: var(--pink);
    font-size: 38px;
    line-height: 41px;
    letter-spacing: -0.8px;
  }
  .decor {
    position: absolute;
    left: 0;
    top: 0;
    width: 848px;
    height: 1200px;
    pointer-events: none;
  }
  .arrow { fill: none; stroke: var(--white); stroke-width: 14; stroke-linecap: round; stroke-linejoin: round; }
  .star { fill: none; stroke: var(--ink); stroke-width: 22; stroke-linecap: round; }
</style>
</head>
<body>
<main class="flyer">
  <h1 class="headline">Lokal<br>&amp;<br>international</h1>

  <p class="offer offer--hiking">Wandertouren -<br>gemeinsam unterwegs<br>sein</p>
  <p class="offer offer--trekking">Trekkingreisen - erfülle<br>Deine Träume</p>
  <p class="offer offer--nature">Naturerlebnisse - Zeit<br>für Dich und Deine Seele</p>

  <div class="film-strip"></div>
  <div class="photo photo--hikers" role="img" aria-label="Foto: zwei Wanderinnen formen mit den Armen ein Herz vor Dolomitengipfeln"></div>
  <div class="photo photo--poppies" role="img" aria-label="Foto: gelber Alpenmohn vor felsiger Berglandschaft"></div>
  <div class="photo photo--valley" role="img" aria-label="Foto: Blick über dunstige Bergketten mit blühendem Rosmarin im Vordergrund"></div>

  <div class="tagline-box">
    <p class="tagline">Inspirationen<br>für Dich<br>und Dein Leben!</p>
  </div>

  <svg class="decor" viewBox="0 0 1414 2000" aria-hidden="true">
    <g class="arrows">
      <path class="arrow" d="M585 660 C650 680 760 680 790 620 C810 580 740 560 705 590 C680 620 760 630 800 600 C840 570 870 530 885 485"/>
      <path class="arrow" d="M815 515 L885 485 L870 555"/>
      <path class="arrow" d="M585 1010 C640 950 820 960 940 1030"/>
      <path class="arrow" d="M905 985 L940 1030 L875 1045"/>
      <path class="arrow" d="M590 1280 C640 1380 690 1440 760 1420 C800 1400 790 1340 740 1340 C690 1350 700 1450 800 1455 C850 1460 880 1455 925 1450"/>
      <path class="arrow" d="M875 1420 L925 1450 L870 1480"/>
    </g>
    <g class="star">
      <path d="M168 1480 L160 1690"/>
      <path d="M85 1505 L255 1660"/>
      <path d="M45 1605 L290 1530"/>
      <path d="M240 1485 L100 1650"/>
    </g>
  </svg>
</main>
</body>
</html>
```